Web Design for Solar Energy Consultancy Company

~ May 3, 2017 Update ~
As our project is rapidly progressing towards its completion, we started building up the list of designs that attracted the most of the team's attention. Additional submittals are still most welcome. Before submitting your proposal, however, we can recommend to review the concepts that received 4 stars as these are the ones that, in our opinion, most closely match the brief's requirements. Thank you!!
~ April 30, 2017 Update ~
The project deadline has been extended to attract a broader design community and to better tailor the final design to the requirements of the project.
A "light", "clean" (minimalistic), professionally looking, unique design is expected. Please, try to avoid industry cliches. Also, please use green, which became another industry cliche, with great caution. The brief provides minimum details to foster creativity. With the same notion in mind, the page content information is not provided.
Thank you for your feedback and support of the project!!
~ April 22, 2017 Update ~
Additional comments after starting receiving more designs:
- your attention to the brief's requirements will be highly appreciated. It is expected that the design is unique - standard, commonly used, images, formats and approaches do not fall under this category. There is no need to "bombard" with slightly different variations of the same design. It is expected that a conceptual (preliminary) design is submitted first, and, after it is reviewed (each design will receive a star rating and, if the star rating is greater than 3, a detailed feedback), the requested changes are implemented. We believe this will allow to approach the design process more efficiently and safe additional time to both the Designers's Community and our company. Thank you for understanding.
Clarification, please submit two variations of a design:
1) 1 page "business card" design that the company will be able to use during its startup stage;
2) the fully functional design (as per the requirements outlined below) for the company to transition to after the start-up period is over. Same design principles as developed for option 1 should be used for this variation.
Additional clarification, please note that the news block will not require images (at least during the start-up stage). It is envisioned to be a news feeder.
~ April 21, 2017 Update ~
Preliminary comments after receiving first designs:
- please try to create a unique design, using common elements wisely. Though such solar energy "attributes" as a solar panel or a bulb are very well recognized and allow quickly identify the nature of the business, they also became so common that in many cases a design may seem very similar to the one of others (Oh!, I've already seen this... effect).
- please try to introduce the company's logo unobtrusively. The size and position of the logo should clearly identify the company, but the message should be subtle, the logo should not distract from the main design. Brask's swoosh did not need to occupy have the screen.
- please use the green color with caution as it was with the company's logo. True, it is a green energy. But there is no need for the color to "scream" about it. Use the amount of green and its tone (avoid acid green) wisely.
--------------------------------------------------------------------------------
1. Main Goal
Develop a website that can represent the company to the industry stakeholders and become its "business card" during the start-up stage.
2. Secondary Goal
Develop a structure of a fully functional website that the "business card" design can eventually be transformed to staying consistent with the original design principles.
3. Key Audience
Varolu Corp. is providing consulting and technical services in the area of Solar Energy. The industry stakeholders include project developers, financial community, governmental bodies, OEMs, and competition.
4. Site Map
- HOME
• About
• Services
• Solar Energy
• News
• Contacts
• Social Media
- SERVICES*
- PROJECTS*
- FINANCE*
- TRAINING*
- SOLAR (ENERGY)*
* Maybe inactive / partially functional during the start-up stage.
5. Technical Specifications
Online brochure website during the start-up stage with a capability to be eventually transformed to a fully functional website while preserving the original design principles.
The design to be appealing, "light", professional, and with an intuitive and easy to navigate interface. Modern coding principles supporting efficiency and security to be utilized. Newest industry trends in website coding will be welcome.
The website to be designed so that it would fit well a computer, tablet, or mobile phone screen of any size. Cross-platform functionality to be taken into consideration to ensure that the website is fully functional on any platform.
Company's logo has already been designed and will be shared with the short-listed designers during the final design stage.
6. Interaction
The website will provide information about the company, our services, and projects. In addition, the industry insight, accumulated knowledge, and most recent trends are planned to be shared with stakeholders and attract and retain the audience.
Interaction with designers during the website development is envisioned to go through the following steps:
a) conceptual design - to be proposed by a designer originally. All conceptual designs will be reviewed and a feedback provided to pre-selected designers;
b) (preliminary and) final design - depending on the level of additional changes required can be broken into two steps. After discussing preliminary designs, company images will be provided to the selected finalists, who will compete with their final proposals.
7. Industry Stakeholders
- https://www.quellbrin.com/power/solar-power.- http://www.pakortavon.com/
- http://www.vellitrazo.com/about/company/
- https://www.oruxem.com/energy/index.html
8. Budget
Defined by the project.
9. Timescale
Defined by the project.
12. Additional Info
- No copy-cats, standard graphics, or cliches please!
- Additional information / clarifications will be gladly provided upon request.
- This specification may be updated throughout the project to reflect discussions with / changes proposed by the Designers community.

```html
<!DOCTYPE html>
<html lang="en">
<head>
<meta charset="utf-8">
<title>Varolu Corp. – Consulting in Renewable Energy</title>
<link rel="stylesheet" href="https://fonts.googleapis.com/css2?family=Comfortaa:wght@500;700&family=Lato:wght@400;700;900&family=Raleway:wght@400;500;600&display=swap">
<style>
:root{
  --green:#3c9c2a;
  --green-dark:#2e7f20;
  --green-footer:#44a436;
  --orange:#f4a300;
  --yellow:#f7c600;
  --text:#555;
  --text-dark:#333;
  --white:#fff;
  --grey-bg:#f1f2f1;
}
*{box-sizing:border-box;margin:0;padding:0}
html,body{width:1200px;height:3396px;overflow:hidden}
body{position:relative;font-family:"Raleway",Arial,sans-serif;color:var(--text);background:var(--white)}
a{color:inherit;text-decoration:none}

/* header */
.site-header{position:absolute;left:0;top:0;width:1200px;height:104px;background:var(--white)}
.brand{position:absolute;left:79px;top:22px;display:flex;align-items:center;gap:12px;font-family:"Lato",sans-serif;font-weight:900;font-size:38px;color:var(--text-dark);letter-spacing:1px}
.brand-dot{width:46px;height:46px;border-radius:50%;background:var(--orange)}
.call{position:absolute;right:88px;top:22px;font-size:15px;color:var(--text-dark)}
.call b{font-weight:500;margin-left:14px}
.main-nav{position:absolute;right:78px;top:62px;display:flex;gap:42px;font-size:16px;color:#666}
.main-nav .active{color:var(--green)}

/* hero */
.hero{position:absolute;left:0;top:104px;width:1200px;height:571px;
  background:linear-gradient(180deg,#0d3d7c 0%,#3d7fc0 40%,#9fc3de 62%,#6f9a3c 78%,#5a8a22 100%)}
.hero-art{position:absolute;left:560px;top:20px;width:560px;height:540px;border-radius:50% 50% 10px 10px;background:radial-gradient(ellipse at 45% 40%,rgba(255,255,255,.45),rgba(120,170,90,.35) 60%,rgba(0,0,0,0) 75%)}
.hero-title{position:absolute;left:79px;top:138px;font-family:"Lato",sans-serif;font-weight:700;font-size:44px;line-height:54px;color:var(--white)}
.hero-text{position:absolute;left:79px;top:262px;width:500px;font-family:"Lato",sans-serif;font-size:19px;line-height:27px;color:var(--white)}
.hero-text b{font-weight:900}
.btn{position:absolute;display:flex;align-items:center;height:50px;background:var(--white);color:var(--green);font-size:18px;padding-left:22px;font-family:"Raleway",sans-serif;font-weight:500}
.btn .chev{position:absolute;right:-14px;top:0;width:50px;height:50px;border-radius:50%;background:var(--green);display:flex;align-items:center;justify-content:center}
.btn.filled{background:var(--green);color:var(--white)}
.btn.filled .chev{background:var(--orange)}

/* section headings */
.sec-title{position:absolute;font-family:"Comfortaa",sans-serif;font-weight:700;font-size:31px;color:var(--green)}

/* committed */
.committed-art{position:absolute;left:79px;top:690px;width:300px;height:300px;border-radius:50%;background:radial-gradient(circle at 50% 45%,#9ccb5a 0%,#6b8a45 45%,#8a6b4a 60%,rgba(255,255,255,0) 72%)}
.body-copy{position:absolute;font-size:14.5px;line-height:24px;color:var(--text)}

/* about */
.about{position:absolute;left:0;top:969px;width:1200px;height:471px;background:linear-gradient(180deg,#fafafa 0%,#eef0ee 80%,#e3eadb 100%)}
.about-art{position:absolute;left:645px;top:36px;width:475px;height:380px;border-radius:45%;background:radial-gradient(ellipse at 40% 55%,#3d7fd0 0%,#7ab2e6 40%,#f3c23a 62%,rgba(255,255,255,0) 74%)}

/* projects */
.project{position:absolute}
.project.p1{background:linear-gradient(180deg,#7aa3cf,#3e5f88)}
.project.p2{background:linear-gradient(180deg,#b6a58a,#4f6f9c)}
.project.p3{background:linear-gradient(135deg,#f4c24a,#27456e)}
.project.p4{background:linear-gradient(180deg,#1e2224,#0e1112);color:var(--white)}
.project.p5{background:linear-gradient(180deg,#8fb0cc,#5c8a4a)}
.project-caption{position:absolute;left:0;top:58px;width:100%;text-align:center;font-size:15px;line-height:24px;font-weight:600;letter-spacing:.5px}

/* consultancy */
.consult{position:absolute;left:0;top:2060px;width:1200px;height:306px;background:linear-gradient(180deg,#f6f8f4 0%,#b9d8ab 45%,#3f9a30 100%)}
.consult-title{position:absolute;left:0;top:66px;width:1200px;text-align:center;font-family:"Comfortaa",sans-serif;font-weight:700;font-size:31px;color:var(--text-dark)}
.consult-text{position:absolute;left:180px;top:124px;width:840px;text-align:center;font-size:14.5px;line-height:24px;color:#444}

/* stakeholders */
.stake{position:absolute;top:2366px;height:260px;width:300px;display:flex;flex-direction:column;align-items:center;justify-content:center;font-family:"Comfortaa",sans-serif;font-weight:700;font-size:21px;color:var(--text-dark);background:linear-gradient(180deg,#fbfbfb,#e3e6e3)}
.stake svg{margin-bottom:22px}
.stake.first{background:linear-gradient(180deg,#e39b3b,#b86a28);align-items:stretch}
.stake-panel{margin:12px;height:236px;background:rgba(246,190,60,.88);text-align:center;padding:30px 18px 0}
.stake-panel h3{font-family:"Comfortaa",sans-serif;font-size:21px;color:var(--text-dark)}
.stake-panel p{font-family:"Raleway",sans-serif;font-weight:500;font-size:14px;line-height:20px;color:#3a3a3a;margin-top:20px}
.stake-panel a{display:inline-block;margin-top:16px;font-family:"Raleway",sans-serif;font-size:15px;text-decoration:underline;color:var(--text-dark)}

/* news */
.news-card{position:absolute;top:2753px;width:369px}
.news-img{height:104px}
.news-date{margin-top:28px;font-size:13px;color:#888;display:flex;align-items:center;gap:8px}
.news-text{margin-top:10px;font-size:14.5px;line-height:22px;color:#555}
.news-arrow{position:absolute;top:2825px;width:32px;height:32px;border-radius:50%;display:flex;align-items:center;justify-content:center}

/* footer */
.site-footer{position:absolute;left:0;top:3000px;width:1200px;height:344px;background:var(--green-footer);color:var(--white)}
.footer-brand{position:absolute;left:79px;top:60px;display:flex;align-items:center;gap:14px;font-family:"Lato",sans-serif;font-weight:900;font-size:44px;letter-spacing:1px}
.footer-brand span.dot{width:52px;height:52px;border-radius:50%;background:rgba(255,255,255,.35)}
.footer-about{position:absolute;left:79px;top:150px;width:320px;font-size:13.5px;line-height:22px}
.socials{position:absolute;left:79px;top:236px;display:flex;gap:18px}
.socials span{width:46px;height:46px;border-radius:50%;background:rgba(255,255,255,.3)}
.socials span.on{background:var(--orange)}
.foot-head{position:absolute;top:60px;font-family:"Comfortaa",sans-serif;font-weight:700;font-size:21px;letter-spacing:1px}
.foot-nav{position:absolute;left:534px;top:104px;list-style:none;font-size:13.5px;line-height:27px}
.foot-nav li::before{content:"• "}
.contact-row{position:absolute;left:817px;display:flex;gap:14px;font-size:14px;line-height:22px}
.bottom-bar{position:absolute;left:0;top:3344px;width:1200px;height:52px;background:linear-gradient(90deg,#f5a500,#f8c400 50%,#f5a500);text-align:center;line-height:52px;font-size:13px;color:var(--text-dark)}
.bottom-bar b{color:var(--white)}
</style>
</head>
<body>

<header class="site-header">
  <div class="brand"><span class="brand-dot"></span>Varolu Corp.</div>
  <div class="call">Call Us Now : <b>+1 555 014 2388</b></div>
  <nav class="main-nav">
    <a class="active">Home</a><a>About Us</a><a>Services</a><a>Projects</a><a>Training</a><a>News</a><a>Contact Us</a>
  </nav>
</header>

<section class="hero">
  <div class="hero-art" role="img" aria-label="Light bulb holding a solar panel and wind turbines on grass, with a green figure beside it, under a blue sky"></div>
  <h1 class="hero-title">CONSULTING IN<br>RENEWABLE ENERGY</h1>
  <p class="hero-text">We provide advice along the entire renewable energy<br>value chain:<br><b>Transactional :</b> project due diligence, feasibility study<br><b>Training :</b> eduction in energy and finance</p>
  <a class="btn" style="left:79px;top:382px;width:210px">LEARN MORE<span class="chev"><svg width="18" height="18" viewBox="0 0 18 18"><path d="M4 4l5 5-5 5M9 4l5 5-5 5" stroke="#fff" stroke-width="2" fill="none"/></svg></span></a>
</section>

<section>
  <div class="committed-art" role="img" aria-label="Floating island of grass with cooling towers and wind turbines"></div>
  <h2 class="sec-title" style="left:460px;top:728px">Let us be committed to solar energy...</h2>
  <div class="body-copy" style="left:421px;top:790px;width:700px">
    <p>We believe we can make a difference to this world, to this very earth on which we live. We have been destroying the forests for whatever reasons for many years. Forests that work much like our lungs, purifying the air and healing us.</p>
    <p style="margin-top:14px">Everyone agrees, that the tree is the best friend for man on this earth. Yet we go on felling them without any qualms. Only when the last tree has been cut and the last river poisoned, we will come to know that we cannot eat money. This beautiful earth needs to be treated with more respect. Let us do it right now...</p>
  </div>
</section>

<section class="about">
  <h2 class="sec-title" style="left:116px;top:116px">About Us</h2>
  <div class="body-copy" style="left:79px;top:172px;width:540px">
    <p>Lorem Ipsum is simply dummy text of the printing and typesetting industry. Lorem Ipsum has been the industry's standard dummy text ever since the 1500s, when an unknown printer took a galley of type and scrambled it to make a type specimen book.</p>
    <p style="margin-top:14px">It has survived not only five centuries, but also the leap into electronic typesetting, remaining essentially unchanged. It was popularised in the 1960s with the release of Letraset sheets containing.</p>
  </div>
  <a class="btn filled" style="left:79px;top:371px;width:200px">READ MORE<span class="chev"><svg width="18" height="18" viewBox="0 0 18 18"><path d="M4 4l5 5-5 5M9 4l5 5-5 5" stroke="#fff" stroke-width="2" fill="none"/></svg></span></a>
  <div class="about-art" role="img" aria-label="Light bulb filled with solar panels and sky, with a cartoon sun beside it"></div>
</section>

<section>
  <h2 class="sec-title" style="left:0;top:1508px;width:1200px;text-align:center">Our Projects</h2>
  <div class="project p1" style="left:77px;top:1569px;width:346px;height:208px" role="img" aria-label="People standing beside a rooftop solar array"></div>
  <div class="project p2" style="left:426px;top:1569px;width:346px;height:208px" role="img" aria-label="Large solar farm in a desert valley"></div>
  <div class="project p3" style="left:776px;top:1569px;width:345px;height:208px" role="img" aria-label="Engineer in a hard hat inspecting solar panels at sunset"></div>
  <div class="project p4" style="left:77px;top:1782px;width:695px;height:208px">
    <p class="project-caption">LOREM IPSUM IS SIMPLY DUMMY TEXT OF PRINTING<br>AND TYPESETTING INDUSTRY.</p>
    <a class="btn filled" style="left:244px;top:118px;width:200px">READ MORE<span class="chev"><svg width="18" height="18" viewBox="0 0 18 18"><path d="M4 4l5 5-5 5M9 4l5 5-5 5" stroke="#fff" stroke-width="2" fill="none"/></svg></span></a>
  </div>
  <div class="project p5" style="left:776px;top:1782px;width:345px;height:208px" role="img" aria-label="Wind turbines along a road through green fields"></div>
</section>

<section class="consult">
  <h2 class="consult-title">Get Free Consultancy About Your Project</h2>
  <p class="consult-text">Integer tincidunt. Cras dapibus. Vivamus elementum semper nisi. Aenean vulputate eleifend tellus. eu, consequat vitae, eleifend ac, enim. Aliquam lorem ante, dapibus in, viverra quis.</p>
  <a class="btn" style="left:460px;top:204px;width:262px">ASK US A QUESTION<span class="chev"><svg width="18" height="18" viewBox="0 0 18 18"><path d="M4 4l5 5-5 5M9 4l5 5-5 5" stroke="#fff" stroke-width="2" fill="none"/></svg></span></a>
</section>

<section>
  <div class="stake first" style="left:0">
    <div class="stake-panel">
      <h3>project developers</h3>
      <p>It has survived not only five centuries, but also the leap into electronic typesetting.</p>
      <a>READ MORE</a>
    </div>
  </div>
  <div class="stake" style="left:300px">
    <svg width="90" height="80" viewBox="0 0 90 80"><circle cx="45" cy="24" r="20" fill="#3c9c2a"/><text x="45" y="32" text-anchor="middle" font-family="Lato,sans-serif" font-weight="900" font-size="24" fill="#fff">$</text><path d="M6 58c12-8 24-6 34 0l18 0c6 0 6 8 0 8H40M4 72c20 6 42 4 62-8l16-10" stroke="#3c9c2a" stroke-width="6" fill="none" stroke-linecap="round"/></svg>
    financial community
  </div>
  <div class="stake" style="left:600px">
    <svg width="130" height="80" viewBox="0 0 130 80"><path d="M20 10h100L100 55H0z" fill="#3c9c2a"/><path d="M45 10L25 55M70 10L50 55M95 10L75 55M10 32h100" stroke="#e9ece9" stroke-width="3"/><path d="M58 55v20M40 76h36" stroke="#3c9c2a" stroke-width="5"/></svg>
    governmental bodies
  </div>
  <div class="stake" style="left:900px">
    <svg width="90" height="80" viewBox="0 0 90 80"><path d="M25 6h40v22c0 12-9 20-20 20S25 40 25 28z" fill="#3c9c2a"/><path d="M25 12H10c0 14 8 20 16 20M65 12h15c0 14-8 20-16 20" stroke="#3c9c2a" stroke-width="5" fill="none"/><path d="M40 48h10v12H40zM28 62h34v10H28z" fill="#3c9c2a"/><path d="M45 14l3 7h7l-6 4 2 7-6-4-6 4 2-7-6-4h7z" fill="#e9ece9"/></svg>
    OEMs And Competition
  </div>
</section>

<section>
  <h2 class="sec-title" style="left:0;top:2692px;width:1200px;text-align:center">Latest News</h2>
  <div class="news-arrow" style="left:137px;border:2px solid #a8c98f"><svg width="12" height="12" viewBox="0 0 12 12"><path d="M8 2L4 6l4 4" stroke="#8bb86a" stroke-width="2" fill="none"/></svg></div>
  <article class="news-card" style="left:229px">
    <div class="news-img" style="background:linear-gradient(180deg,#5f9fe0,#7bbf4a)" role="img" aria-label="Solar panels and trees under a rainbow"></div>
    <div class="news-date"><svg width="14" height="14" viewBox="0 0 14 14"><rect x="1" y="2" width="12" height="11" fill="none" stroke="#aaa"/><path d="M1 5h12" stroke="#aaa"/></svg>10 April,2017</div>
    <p class="news-text">Lorem ipsum dolor sit amet, consectetur adipiscing elit, sed do eiusmod tempor...</p>
  </article>
  <article class="news-card" style="left:604px">
    <div class="news-img" style="background:linear-gradient(180deg,#4d7fc4,#234a86)" role="img" aria-label="Solar powered aircraft in flight over the sea"></div>
    <div class="news-date"><svg width="14" height="14" viewBox="0 0 14 14"><rect x="1" y="2" width="12" height="11" fill="none" stroke="#aaa"/><path d="M1 5h12" stroke="#aaa"/></svg>08 March,2017</div>
    <p class="news-text">Lorem ipsum dolor sit amet, consectetur adipiscing elit, sed do eiusmod tempor...</p>
  </article>
  <div class="news-arrow" style="left:1032px;background:#222"><svg width="12" height="12" viewBox="0 0 12 12"><path d="M4 2l4 4-4 4" stroke="#fff" stroke-width="2" fill="none"/></svg></div>
</section>

<footer class="site-footer">
  <div class="footer-brand"><span class="dot"></span>Varolu Corp.</div>
  <p class="footer-about">Lorem Ipsum is simply dummy text of the printing and typesetting industry. Lorem Ipsum has been the industry.</p>
  <div class="socials"><span class="on"></span><span></span><span></span><span></span></div>

  <h3 class="foot-head" style="left:534px">Navigation</h3>
  <ul class="foot-nav">
    <li>Home</li><li>About US</li><li>Services</li><li>Solar Energy</li><li>News</li><li>Contact Us</li><li>Training</li>
  </ul>

  <h3 class="foot-head" style="left:817px">Contact Us</h3>
  <div class="contact-row" style="top:108px"><svg width="18" height="18" viewBox="0 0 18 18"><path d="M9 1v16M2 5h14M2 11h14" stroke="#fff" stroke-width="2"/></svg><span>Varolu Corp.<br>48 Halden Row, Suite 5,<br>Marrowfield, 30412.</span></div>
  <div class="contact-row" style="top:200px"><svg width="18" height="18" viewBox="0 0 18 18"><path d="M4 1l3 4-2 2c1 3 3 5 6 6l2-2 4 3-2 3C8 17 1 10 1 3z" fill="#fff"/></svg><span>+1 555 014 2388</span></div>
  <div class="contact-row" style="top:250px"><svg width="18" height="18" viewBox="0 0 18 18"><rect x="1" y="4" width="16" height="11" fill="none" stroke="#fff" stroke-width="1.6"/><path d="M1 4l8 6 8-6" stroke="#fff" stroke-width="1.6" fill="none"/></svg><span>varolugroup@sunfieldmail.com</span></div>
</footer>

<div class="bottom-bar">© 2017 <b>VAROLU CORP.</b> All rights reserved.</div>

</body>
</html>
```